ZMobvra - Tenant Place Services

Want Quality Tenants?!

Tenant Placement is a service that allows landlords to leave the stress of filling vacancies behind.
zMobvra provides landlords, investors and property manager's a system to occupy vacancies with qualified tenants Faster, Cheaper, Easier
zMobvra takes the hassle out of the rental process from searching for tenants to move-in inspections.

Reason: I'm extending the deadline because I want to give other designers an opportunity to submit and I have a couple designs that I'm awaiting current designers to resubmit some designs.

```html
<!DOCTYPE html>
<html lang="en">
<head>
<meta charset="utf-8">
<title>zMobvra – Need Tenants?!</title>
<link rel="stylesheet" href="https://fonts.googleapis.com/css2?family=Arimo:wght@400;700&display=swap">
<style>
  :root {
    --night-dark: #0d0d0f;
    --night-mid: #3a3b3f;
    --leaf-green: #a6c933;
    --leaf-light: #c9df7a;
    --leaf-pale: #e6f1bd;
    --band-dark: rgba(10, 12, 12, 0.82);
    --white: #ffffff;
    --brand-grey: #5c5e60;
  }
  html, body {
    margin: 0;
    padding: 0;
    overflow: hidden;
    background: #ffffff;
  }
  .ad {
    position: relative;
    width: 1200px;
    height: 840px;
    overflow: hidden;
    font-family: "Arimo", Arial, sans-serif;
  }
  .city-photo {
    position: absolute;
    inset: 0;
    background:
      radial-gradient(ellipse at 70% 35%, rgba(200,200,205,0.35), transparent 55%),
      linear-gradient(180deg, #55565b 0%, var(--night-mid) 30%, #1e1f22 65%, var(--night-dark) 100%);
  }
  .leaf-glow {
    position: absolute;
    left: -260px;
    top: -80px;
    width: 900px;
    height: 1000px;
    background: radial-gradient(ellipse at 48% 46%,
      var(--leaf-light) 0%, var(--leaf-green) 38%, rgba(166,201,51,0.55) 55%, rgba(166,201,51,0) 72%);
  }
  .brand-badge {
    position: absolute;
    left: -47px;
    top: 165px;
    width: 430px;
    height: 430px;
    border-radius: 50%;
    background: var(--white);
    box-shadow: 0 0 0 16px var(--leaf-pale);
  }
  .brand-name {
    position: absolute;
    left: 0;
    top: 452px;
    width: 250px;
    text-align: center;
    font-weight: 400;
    font-size: 62px;
    color: var(--brand-grey);
    letter-spacing: 2px;
  }
  .headline-band {
    position: absolute;
    left: 400px;
    top: 354px;
    width: 800px;
    height: 138px;
    background: var(--leaf-green);
    display: flex;
    align-items: center;
    justify-content: flex-end;
    padding-right: 66px;
    box-sizing: border-box;
  }
  .headline {
    margin: 0;
    font-weight: 400;
    font-size: 74px;
    color: var(--white);
  }
  .offer-band {
    position: absolute;
    left: 450px;
    top: 492px;
    width: 750px;
    height: 168px;
    background: var(--band-dark);
    display: flex;
    flex-direction: column;
    justify-content: center;
    align-items: flex-end;
    padding-right: 66px;
    box-sizing: border-box;
  }
  .offer-line {
    margin: 0;
    font-weight: 700;
    font-size: 37px;
    line-height: 50px;
    color: var(--white);
  }
  .web-address {
    position: absolute;
    right: 60px;
    top: 766px;
    margin: 0;
    font-weight: 700;
    font-size: 31px;
    color: var(--white);
  }
</style>
</head>
<body>
  <main class="ad">
    <div class="city-photo" role="img" aria-label="Black and white photograph of a city skyline at night with lit skyscrapers"></div>
    <div class="leaf-glow" role="img" aria-label="Green leaf-like swoosh decoration radiating from the brand badge"></div>

    <div class="brand-badge"></div>
    <div class="brand-name">zMobvra</div>

    <div class="headline-band">
      <h1 class="headline">NEED TENANTS?!</h1>
    </div>

    <div class="offer-band">
      <p class="offer-line">FILL YOUR VACANCY</p>
      <p class="offer-line">FASTER, EASIER, CHEAPER</p>
    </div>

    <p class="web-address">@ ZMOBVRA.COM</p>
  </main>
</body>
</html>
```